Coastal keel catch

Hi everyone,
I’m operating a fishing boat targeting sought after deep water fish species off the southern coast of wa, where the product is sold from the boat directly to restaurants around the region. We fish with rods and not nets ensuring the fish are caught in an eco friendly manner maintaining longevity of the industry. This fishery takes place along a rugged coastline and wild oceans where conditions are not always favourable. Hoping for a design that can encompass these elements and also the care taken during harvest of the product ensuring quality of the fish and freshest fillets. I’ve attached photos of some targeted species, blue eye trevalla and dhufish, nannigai and pink snapper which would be nice to include
Thanks marcus

Target Market(s)

Restaurants/ seafood processors

Contact Information for Business Card

Top quality line caught scalefish, sustainably sourced from the pristine waters of south west WA
Contact marcus leaf 0417586204

Requirements
Must have
• Catchy design yet simple
Appealing and promote values of business
-premium quality and freshness
-minimal impact on environment
Nice to have
• The wa dhufish incorporated in the logo. Wendaroolures.example have a few good examples as theirs

```html
<!DOCTYPE html>
<html lang="en">
<head>
<meta charset="utf-8">
<title>Coastal Keel Catch – Business Card</title>
<link rel="stylesheet" href="https://fonts.googleapis.com/css2?family=EB+Garamond:wght@400;500&display=swap">
<style>
  :root {
    --backdrop: #e9e9e7;
    --card-paper: #fbfbf9;
    --ink-navy: #0f1d3a;
  }
  * { margin: 0; padding: 0; box-sizing: border-box; }
  html, body {
    width: 1200px;
    height: 800px;
    overflow: hidden;
    background: var(--backdrop);
  }
  .stage {
    position: relative;
    width: 1200px;
    height: 800px;
  }
  .business-card {
    position: absolute;
    left: 150px;
    top: 150px;
    width: 900px;
    height: 500px;
    background: var(--card-paper);
    box-shadow: 0 10px 30px rgba(0, 0, 0, 0.12), 0 2px 6px rgba(0, 0, 0, 0.08);
    font-family: "EB Garamond", "Times New Roman", serif;
    color: var(--ink-navy);
  }
  .tagline {
    position: absolute;
    left: 130px;
    top: 62px;
    line-height: 1;
  }
  .tagline-small {
    display: block;
    font-size: 19px;
    letter-spacing: 0.2px;
    margin-bottom: 2px;
  }
  .tagline-large {
    display: block;
    font-size: 38px;
    letter-spacing: 0.6px;
    margin-bottom: 3px;
  }
  .brand-name {
    position: absolute;
    left: 72px;
    top: 318px;
    font-size: 58px;
    font-weight: 400;
    line-height: 0.9;
    letter-spacing: 0.5px;
  }
  .brand-name span { display: block; }
  .brand-name .indent { padding-left: 18px; }
  .contact-block {
    position: absolute;
    left: 610px;
    top: 356px;
    line-height: 1;
  }
  .contact-label {
    display: block;
    font-size: 19px;
    letter-spacing: 1.5px;
    margin-left: 22px;
    margin-bottom: 4px;
  }
  .contact-name {
    display: block;
    font-size: 46px;
    letter-spacing: 0.5px;
  }
  .contact-phone {
    display: block;
    font-size: 19px;
    letter-spacing: 2.5px;
    margin-top: 4px;
  }
  .edge-dots {
    position: absolute;
    display: flex;
    flex-direction: column;
    gap: 26px;
  }
  .edge-dots i {
    display: block;
    width: 3px;
    height: 3px;
    border-radius: 50%;
    background: var(--ink-navy);
  }
  .edge-dots.left { left: 40px; top: 200px; }
  .edge-dots.right { right: 40px; top: 300px; }
</style>
</head>
<body>
<div class="stage">
  <article class="business-card">
    <p class="tagline">
      <span class="tagline-small">Top quality line</span>
      <span class="tagline-large">caught scalefish,</span>
      <span class="tagline-small">Sustainably harvested from the pristine waters of</span>
      <span class="tagline-large">south west WA.</span>
    </p>

    <div class="edge-dots left"><i></i><i></i><i></i></div>
    <div class="edge-dots right"><i></i><i></i><i></i><i></i></div>

    <h1 class="brand-name">
      <span>Coastal</span>
      <span class="indent">Keel Catch</span>
    </h1>

    <p class="contact-block">
      <span class="contact-label">Contact</span>
      <span class="contact-name">Marcus Leaf</span>
      <span class="contact-phone">0417586204</span>
    </p>
  </article>
</div>
</body>
</html>
```